Brightpath EAP 2 x Flyer with Poster

Brightpath is an award-winning organisation providing dynamic and creative ways for children, young people, adults and families to make positive change and achieve fulfilling lives.
We are launching into a new area of business and starting to offer organisations Employee Assistance Program (EAP). To launch this service we need 2 flyers and a poster:
- 1 x flyer for employers
- 1 x flyer for employees
- 1 x poster (A3) for employees to be displayed around the office.
For the flyers we are after an a4 colour double sided flyer in either a A4 tri-fold to DL format or A4 bi-fold to A5 format. We are looking for a design that is simple and dynamic whilst keeping in line with our branding.
The winning designs will need to be hi-res and ready for print and also a lower res version suitable to email.
I have attached a number of files to provide further background, including:
• I have attached 3 x word doc of copy for each (2 x flyer / 1 x poster)
• Brand Guidelines
• Logo
• Our clinic flyer recently produced by a ArtHive designer for our clinic area of the business. These flyers do not have to be exactly the same as this one but should appear to be from the same organisation although a different service.
Generally we like our designs to be clear and simple.
Please don't hesitate to reach out with any Q's.

```html
<!DOCTYPE html>
<html lang="en">
<head>
<meta charset="utf-8">
<title>Brightpath – Employee Assistance Program Poster</title>
<link href="https://fonts.googleapis.com/css2?family=Poppins:wght@400;500;600;700&display=swap" rel="stylesheet">
<style>
  :root{
    --teal:#7f9ea2;
    --teal-title:#7a9a9f;
    --salmon:#d6ad97;
    --sage:#7c9a82;
    --ink:#333637;
    --paper:#ffffff;
  }
  *{margin:0;padding:0;box-sizing:border-box}
  html,body{width:701px;height:1200px;overflow:hidden;background:var(--paper)}
  body{font-family:"Poppins",sans-serif;color:var(--ink)}
  .poster{position:relative;width:701px;height:1200px;overflow:hidden;background:var(--paper)}
  .backdrop{position:absolute;inset:0}
  .brand{position:absolute;left:32px;top:52px;display:flex;align-items:center;gap:10px}
  .brand-square{width:34px;height:34px;background:var(--teal)}
  .brand-name{font-size:42px;font-weight:500;color:var(--ink);line-height:1}
  .title{position:absolute;left:24px;top:330px;font-weight:700;color:var(--teal-title);font-size:41px;line-height:58px}
  .title small{font-size:26px;font-weight:600}
  .subtitle{position:absolute;left:24px;top:518px;font-size:23px;font-weight:500;line-height:34px;text-transform:uppercase;color:var(--ink)}
  .info{position:absolute;left:24px;width:318px}
  .info h2{font-size:17px;font-weight:600;color:var(--salmon);margin-bottom:5px}
  .info h2 span{color:var(--teal-title)}
  .info p{font-size:11px;line-height:1.3;letter-spacing:-.1px;color:var(--ink)}
  .divider{position:absolute;left:24px;width:192px;height:1.5px;background:var(--sage)}
  .services{position:absolute;left:350px;width:351px;top:566px;text-align:center;color:var(--paper)}
  .services h2{font-size:19px;font-weight:600;color:var(--salmon)}
  .services p{font-size:11.3px;line-height:1.25;margin-top:4px;padding:0 30px}
  .service-grid{position:absolute;left:364px;top:648px;width:330px;display:grid;grid-template-columns:98px 128px 100px;row-gap:14px;color:var(--paper)}
  .service-grid li{list-style:none;font-size:11.6px;font-weight:500;line-height:1.15;padding-left:14px;position:relative}
  .service-grid li::before{content:"»";position:absolute;left:0;top:-1px;color:var(--salmon);font-weight:600}
  .calendar-art{position:absolute;left:386px;top:894px;width:100px;height:124px;border-radius:6px;background:linear-gradient(160deg,#c9d6d8,#9fb4b7)}
  .appointment{position:absolute;left:508px;top:906px;width:180px;color:var(--paper)}
  .appointment h2{font-size:17px;font-weight:600;line-height:1.25;color:var(--salmon)}
  .appointment p{font-size:11.3px;line-height:1.2;margin-top:8px}
  .contact{position:absolute;left:408px;top:1052px;width:240px;height:86px;border-radius:8px;background:var(--salmon);color:var(--paper);padding:12px 0 0 26px}
  .contact-phone{display:flex;align-items:center;gap:8px;font-size:26px;font-weight:600;line-height:1.15}
  .contact-mail{display:flex;align-items:center;gap:8px;font-size:18px;line-height:1.3}
  .footer{position:absolute;left:28px;top:1152px;display:flex;gap:30px;color:var(--paper);font-size:12px;line-height:1.3}
  .footer-item{display:flex;align-items:flex-start;gap:8px}
  .footer-web{font-weight:600}
</style>
</head>
<body>
<div class="poster">
  <svg class="backdrop" width="701" height="1200" viewBox="0 0 701 1200" aria-hidden="true">
    <defs>
      <linearGradient id="photoTone" x1="0" y1="0" x2="1" y2="0.3">
        <stop offset="0" stop-color="#eef0f1"/>
        <stop offset="0.3" stop-color="#e6e7e8"/>
        <stop offset="0.55" stop-color="#8a8a8a"/>
        <stop offset="0.8" stop-color="#5f5f5f"/>
        <stop offset="1" stop-color="#a5a5a5"/>
      </linearGradient>
    </defs>
    <rect width="701" height="1200" fill="#ffffff"/>
    <rect x="350" y="400" width="351" height="760" fill="var(--teal)"/>
    <path d="M0 1140 L470 1140 L560 1200 L0 1200 Z" fill="var(--sage)"/>
    <path d="M470 1140 L701 1060 L701 1200 L560 1200 Z" fill="#ffffff"/>
    <path d="M600 1200 L701 1148 L701 1200 Z" fill="var(--salmon)"/>
    <path d="M468 1134 h120 l-10 12 h-100 z" fill="var(--teal)"/>
    <path d="M-10 150 L480 470 Q600 546 710 446 L710 -10 L-10 -10 Z" fill="url(#photoTone)" role="img" aria-label="Black-and-white photo of five smiling young colleagues gathered around a laptop"/>
    <path d="M-10 150 L480 470 Q600 546 710 446" transform="translate(0,16)" fill="none" stroke="#ffffff" stroke-width="38"/>
    <path d="M-10 150 L480 470 Q600 546 710 446" fill="none" stroke="var(--salmon)" stroke-width="22"/>
  </svg>

  <div class="brand"><span class="brand-square"></span><span class="brand-name">Brightpath</span></div>

  <h1 class="title">Employee<br>Assistance<br>Program <small>(EAP)</small></h1>
  <div class="subtitle">Counselling for<br>work related or<br>personal issues</div>

  <section class="info" style="top:660px">
    <h2>Who Pays for <span>the Service?</span></h2>
    <p>Your employer will pay for an agreed number of sessions. You are not required to pay for using the Brightpath EAP service. The number of available sessions depends on the agreement we have with your employer.</p>
  </section>
  <div class="divider" style="top:774px"></div>
  <section class="info" style="top:792px">
    <h2>Is it <span>Confidential?</span></h2>
    <p>All employee personal information collated by Brightpath during the provision of counselling services will remain confidential and secure except when subpoenaed by a court or failure to disclose the information would place the employee and/or another person at risk. Confidentiality and limitations of confidentiality are explained to employees at the beginning of the counselling process</p>
  </section>
  <div class="divider" style="top:950px"></div>
  <section class="info" style="top:968px">
    <h2>About Brightpath</h2>
    <p>Brightpath provides a confidential and effective counselling process that is solution-focused and practical. The service is aimed at enhancing wellbeing and mental health, and can be accessed via face-to-face consultations, and by Telehealth or phone. Accessing assistance is an act of independence and strength which can empower you to make positive changes in your life.</p>
  </section>

  <section class="services">
    <h2>Counselling Services</h2>
    <p>EAP is provided for a variety of personal, emotional and work-related matters including:</p>
  </section>
  <ul class="service-grid">
    <li>Anxiety</li><li>Self-esteem</li><li>Bullying</li>
    <li>Domestic violence</li><li>Grief &amp; bereavement</li><li>Sexual harassment</li>
    <li>Critical incidents</li><li>Schooling and study difficulties</li><li>Interpersonal relationships</li>
    <li>Stress &amp; burnout</li><li>Workplace conflict or disharmony</li><li>Substance misuse</li>
    <li>Depression &amp; emotional wellbeing</li><li>Coping with organisational change</li><li>Reactions to traumatic or distressing events</li>
  </ul>

  <div class="calendar-art" role="img" aria-label="Illustration of two people beside a large calendar with a ticked date"></div>
  <section class="appointment">
    <h2>How do I make an EAP Appointment?</h2>
    <p>You can make a confidential appointment directly with Brightpath through our direct line on</p>
  </section>

  <div class="contact">
    <div class="contact-phone">
      <svg width="12" height="12" viewBox="0 0 24 24" aria-hidden="true"><path d="M6.6 10.8a15 15 0 0 0 6.6 6.6l2.2-2.2a1 1 0 0 1 1-.25 11.4 11.4 0 0 0 3.6.6 1 1 0 0 1 1 1V20a1 1 0 0 1-1 1A17 17 0 0 1 3 4a1 1 0 0 1 1-1h3.5a1 1 0 0 1 1 1c0 1.25.2 2.45.6 3.6a1 1 0 0 1-.25 1z" fill="#fff"/></svg>
      03 9000 4821
    </div>
    <div class="contact-mail">
      <svg width="11" height="9" viewBox="0 0 22 16" aria-hidden="true"><rect width="22" height="16" rx="2" fill="#fff"/><path d="M1 1l10 8 10-8" fill="none" stroke="var(--salmon)" stroke-width="2"/></svg>
      clinic@brightpath.au
    </div>
  </div>

  <footer class="footer">
    <div class="footer-item">
      <svg width="10" height="13" viewBox="0 0 20 26" aria-hidden="true"><path d="M10 0a10 10 0 0 0-10 10c0 7 10 16 10 16s10-9 10-16A10 10 0 0 0 10 0z" fill="#fff"/><circle cx="10" cy="10" r="3.5" fill="var(--sage)"/></svg>
      <span>Harbourview Building<br>42 Larkspur Ave, Elmwood VIC 3999</span>
    </div>
    <div class="footer-item footer-web">
      <svg width="11" height="11" viewBox="0 0 22 22" aria-hidden="true"><circle cx="11" cy="11" r="9.5" fill="none" stroke="#fff" stroke-width="2"/><path d="M1.5 11h19M11 1.5c-5 5-5 14 0 19M11 1.5c5 5 5 14 0 19" fill="none" stroke="#fff" stroke-width="1.5"/></svg>
      <span>brightpath.au</span>
    </div>
  </footer>
</div>
</body>
</html>
```